Meadowgate Bus Card

i own a building in the bronx ny - its called "Meadowgate HDFC"i want a classy logo / business card - nothing too religuous but it is like a family there - its a large apartment building - colors i like dark red, black, medium shade of gray also reg business card stuff tel # 914-552-3917 address 3182 Larkwell Ave Bronx NY 10472 Email fijosh@aol.comslogan - " Many doors, one family "i can send u a picture of the building for the backside

```html
<!DOCTYPE html>
<html lang="en">
<head>
<meta charset="utf-8">
<title>Meadowgate HDFC – Business Card Options</title>
<link href="https://fonts.googleapis.com/css2?family=Ubuntu:wght@400;700&family=Cormorant+Garamond:wght@500&family=Montserrat:wght@400;500;700&display=swap" rel="stylesheet">
<style>
  :root {
    --paper: #ffffff;
    --gray-card: #d1d2d4;
    --ink: #2b2b2b;
    --slate: #555557;
    --mid-gray: #8a8b8d;
    --red: #cf3a3e;
    --dark-red: #9c2f2b;
    --rust: #c0432f;
    --black: #231f20;
    --white: #ffffff;
  }
  * { box-sizing: border-box; margin: 0; padding: 0; }
  html, body {
    width: 1200px; height: 713px; overflow: hidden;
    background: var(--paper);
  }
  .sheet { position: relative; width: 1200px; height: 713px; }

  .card {
    position: absolute; width: 520px; height: 310px;
    display: flex; flex-direction: column; align-items: center;
    text-align: center; overflow: hidden;
  }
  .card--gray  { left: 70px;  top: 28px;  background: var(--gray-card); }
  .card--white { left: 610px; top: 28px;  background: var(--paper); border: 2px solid var(--black); }
  .card--split { left: 70px;  top: 380px; background: var(--black); }
  .card--black { left: 610px; top: 380px; background: var(--black); }

  .brand {
    width: 100%; display: flex; flex-direction: column; align-items: center;
    padding-top: 40px;
  }
  .brand__name {
    font-family: "Ubuntu", sans-serif; font-weight: 700;
    font-size: 44px; letter-spacing: 3px; line-height: 1;
    text-transform: uppercase;
  }
  .brand__rule { width: 440px; height: 3px; margin-top: 10px; }
  .brand__tag {
    display: flex; align-items: center; gap: 14px;
    width: 440px; margin-top: 6px;
  }
  .brand__tag::before, .brand__tag::after {
    content: ""; flex: 1; height: 2px; background: currentColor;
  }
  .brand__hdfc {
    font-family: "Ubuntu", sans-serif; font-weight: 700;
    font-size: 20px; letter-spacing: 4px;
  }
  .slogan {
    margin-top: 14px; font-size: 27px; letter-spacing: 1.5px;
    text-transform: uppercase;
  }
  .contact {
    margin-top: auto; padding-bottom: 40px;
    font-family: "Montserrat", sans-serif; font-style: normal; font-size: 13px;
    letter-spacing: 0.8px; line-height: 1.9; text-transform: uppercase;
  }

  /* gray card */
  .card--gray .brand__name { color: var(--ink); }
  .card--gray .brand__rule { background: var(--red); }
  .card--gray .brand__tag  { color: var(--ink); margin-top: 8px; }
  .card--gray .brand__tag::before, .card--gray .brand__tag::after { opacity: 0; }
  .card--gray .brand__hdfc { color: var(--ink); }
  .card--gray .slogan { font-family: "Cormorant Garamond", serif; font-weight: 500; color: var(--slate); font-size: 29px; margin-top: 10px; }
  .card--gray .contact { color: var(--ink); }

  /* white card */
  .card--white .brand__name { color: var(--slate); }
  .card--white .brand__rule { display: none; }
  .card--white .brand__tag  { color: var(--ink); margin-top: 16px; }
  .card--white .brand__hdfc { color: var(--mid-gray); }
  .card--white .slogan { font-family: "Montserrat", sans-serif; font-weight: 400; color: var(--slate); font-size: 24px; }
  .card--white .contact { color: var(--rust); }

  /* red + black card */
  .card--split .brand { background: var(--dark-red); height: 188px; }
  .card--split .brand__name { color: var(--white); }
  .card--split .brand__rule { display: none; }
  .card--split .brand__tag  { color: var(--black); margin-top: 14px; }
  .card--split .brand__hdfc { color: var(--white); }
  .card--split .slogan { font-family: "Montserrat", sans-serif; font-weight: 400; color: var(--white); font-size: 23px; }
  .card--split .contact { color: var(--white); padding-bottom: 34px; }

  /* black card */
  .card--black .brand__name { color: var(--red); }
  .card--black .brand__rule { display: none; }
  .card--black .brand__tag  { color: var(--white); margin-top: 18px; }
  .card--black .brand__hdfc { color: var(--mid-gray); }
  .card--black .slogan { font-family: "Montserrat", sans-serif; font-weight: 700; color: var(--red); font-size: 22px; }
  .card--black .contact { color: var(--white); }
</style>
</head>
<body>
<main class="sheet">

  <section class="card card--gray" aria-label="Business card, gray option">
    <div class="brand">
      <p class="brand__name">Meadowgate</p>
      <div class="brand__rule"></div>
      <p class="brand__tag"><span class="brand__hdfc">HDFC</span></p>
    </div>
    <p class="slogan">Many doors, one family</p>
    <address class="contact">
      3182 Larkwell Ave Bronx NY 10472<br>
      #914.552.3917&nbsp;&nbsp;&nbsp;kemarv@plonkmail.test
    </address>
  </section>

  <section class="card card--white" aria-label="Business card, white option">
    <div class="brand">
      <p class="brand__name">Meadowgate</p>
      <div class="brand__rule"></div>
      <p class="brand__tag"><span class="brand__hdfc">HDFC</span></p>
    </div>
    <p class="slogan">Many doors, one family</p>
    <address class="contact">
      3182 Larkwell Ave Bronx NY 10472<br>
      #914.552.3917&nbsp;&nbsp;&nbsp;kemarv@plonkmail.test
    </address>
  </section>

  <section class="card card--split" aria-label="Business card, red and black option">
    <div class="brand">
      <p class="brand__name">Meadowgate</p>
      <div class="brand__rule"></div>
      <p class="brand__tag"><span class="brand__hdfc">HDFC</span></p>
      <p class="slogan">Many doors, one family</p>
    </div>
    <address class="contact">
      3182 Larkwell Ave Bronx NY 10472<br>
      #914.552.3917&nbsp;&nbsp;&nbsp;kemarv@plonkmail.test
    </address>
  </section>

  <section class="card card--black" aria-label="Business card, black option">
    <div class="brand">
      <p class="brand__name">Meadowgate</p>
      <div class="brand__rule"></div>
      <p class="brand__tag"><span class="brand__hdfc">HDFC</span></p>
    </div>
    <p class="slogan">Many doors, one family</p>
    <address class="contact">
      3182 Larkwell Ave Bronx NY 10472<br>
      #914.552.3917&nbsp;&nbsp;&nbsp;kemarv@plonkmail.test
    </address>
  </section>

</main>
</body>
</html>
```